Casa Verdant business card
Indoor Environmental Specialists
Professional
Rob Tallowmere
President
2917 North Quailbrook Ave Unit 248
Pinecrest Harbor FL, 33718
rob@casaverdantcrew.com
www.casaverdantcrew.com
QTX LKPV391 DWBE PNGH862
Serving:
Southeast Florida and the Caribbean
Indoor Mold Screen Assessments.
Indoor Air Quality Testing.
Mold Remediation Contractor.
Moisture Intrusion Surveys.
Thermal Imaging Inspection.
UV Air Sanitizer Sales & Service.
Casa Verdant Logo
Casa Verdant Logo On The Left Side

```html
<!DOCTYPE html>
<html lang="en">
<head>
<meta charset="utf-8">
<title>Casa Verdant Stationery</title>
<link rel="stylesheet" href="https://fonts.googleapis.com/css2?family=Open+Sans:wght@400;600;700&display=swap">
<style>
:root{
  --bg:#ecebe8;
  --paper:#ffffff;
  --navy:#0b3a78;
  --blue:#1560b5;
  --sky:#3a9be0;
  --green:#6fb52c;
  --lime:#a6d14a;
  --ink:#33475f;
  --muted:#7b8794;
  --faint:#e6edf3;
  --line:#d6dce2;
}
*{box-sizing:border-box;margin:0;padding:0}
html,body{width:1200px;height:439px;overflow:hidden;background:var(--bg);font-family:'Open Sans',sans-serif;color:var(--ink)}
.stage{position:relative;width:1200px;height:439px}
.piece{position:absolute;background:var(--paper);box-shadow:0 2px 6px rgba(0,0,0,.25);overflow:hidden}
.brand{display:flex;align-items:center;gap:4px;font-weight:700;color:var(--blue);white-space:nowrap}
.brand .dot{border-radius:50%;background:var(--green);flex:none}
.band{position:absolute;left:0;bottom:0;width:100%;display:block}

/* business card front */
.card-front{left:18px;top:66px;width:98px;height:70px;background:linear-gradient(135deg,var(--navy),var(--blue));color:#fff}
.card-front .who{position:absolute;left:5px;top:6px;width:62px;font-size:3.6px;line-height:1.4}
.card-front .who b{font-size:5px;display:block}
.card-front .contact{position:absolute;left:5px;top:28px;width:62px;font-size:3.2px;line-height:1.45}
.card-front .greenbar{position:absolute;right:0;top:0;width:27px;height:100%;background:linear-gradient(180deg,var(--lime),var(--green))}
.card-front .seal{position:absolute;right:4px;top:25px;width:19px;height:19px;border-radius:50%;background:#fff;border:2px solid var(--sky)}

/* business card services side */
.card-list{left:18px;top:176px;width:98px;height:70px}
.card-list ul{list-style:none;position:absolute;left:6px;top:7px;font-size:3.5px;line-height:1.65;color:var(--ink)}
.card-list li::before{content:"";display:inline-block;width:3px;height:3px;background:var(--green);border-radius:50%;margin-right:3px;vertical-align:middle}
.card-list .logo-disc{position:absolute;right:6px;top:18px;width:22px;height:22px;border-radius:50%;background:var(--sky)}

/* business card logo side */
.card-logo{left:18px;top:296px;width:98px;height:70px;background:linear-gradient(160deg,var(--navy),var(--blue))}
.card-logo .plate{position:absolute;left:10px;top:14px;width:78px;height:38px;background:#fff;border-radius:4px;display:flex;align-items:center;justify-content:center}
.card-logo .plate .brand{font-size:8px}
.card-logo .plate .dot{width:9px;height:9px}

/* letterheads */
.letter{top:19px;width:282px;height:389px}
.letter-a{left:198px}
.letter-b{left:502px}
.letter .head{position:absolute;left:16px;top:16px}
.letter .head .brand{font-size:10px}
.letter .head .dot{width:15px;height:15px}
.letter .tag{font-size:4.5px;color:var(--muted);margin-left:19px}
.letter .addr{position:absolute;left:122px;top:18px;font-size:4px;line-height:1.5;color:var(--muted)}
.letter .addr-right{position:absolute;left:200px;top:18px;font-size:4px;line-height:1.5;color:var(--muted)}
.letter .watermark{position:absolute;left:66px;top:120px;width:150px;height:150px;border-radius:50%;border:3px solid var(--faint);display:flex;align-items:center;justify-content:center;font-weight:700;font-size:16px;color:var(--faint)}
.letter-b .head{left:74px;top:22px}
.letter .foot{position:absolute;left:0;bottom:7px;width:100%;text-align:center;font-size:4px;color:#fff}

/* envelopes */
.env{position:absolute}
.env .flap{position:absolute;left:0;top:0;width:100%;height:100%;display:block}
.env .seal{position:absolute;width:16px;height:16px;border-radius:50%;background:var(--sky);border:2px solid #fff;transform:translateX(-50%)}
.env-green{left:842px;top:19px;width:344px;height:88px;z-index:1}
.env-blue{left:842px;top:100px;width:344px;height:86px;z-index:2}
.env-plain{left:826px;top:178px;width:360px;height:82px;z-index:3}
.env-front{left:808px;top:252px;width:378px;height:156px;z-index:4}
.env-green .seal{left:172px;top:56px}
.env-blue .seal{left:172px;top:46px}
.env-front .head{position:absolute;left:12px;top:60px}
.env-front .head .brand{font-size:9px}
.env-front .head .dot{width:13px;height:13px}
.env-front .addr{position:absolute;left:12px;top:80px;font-size:4px;line-height:1.5;color:var(--muted)}
</style>
</head>
<body>
<main class="stage">

  <section class="piece card-front" aria-label="Business card front">
    <div class="greenbar"></div>
    <div class="seal"></div>
    <p class="who"><b>Rob Tallowmere</b>President<br>Indoor Environmental Specialists</p>
    <p class="contact">2917 North Quailbrook Ave Unit 248<br>Pinecrest Harbor FL, 33718<br>rob@casaverdantcrew.com<br>www.casaverdantcrew.com<br>QTX LKPV391 DWBE PNGH862</p>
  </section>

  <section class="piece card-list" aria-label="Business card services side">
    <ul>
      <li>Indoor Mold Screen Assessments.</li>
      <li>Indoor Air Quality Testing.</li>
      <li>Mold Remediation Contractor.</li>
      <li>Moisture Intrusion Surveys.</li>
      <li>Thermal Imaging Inspection.</li>
      <li>UV Air Sanitizer Sales &amp; Service.</li>
    </ul>
    <div class="logo-disc"></div>
    <svg class="band" viewBox="0 0 98 12" height="12" preserveAspectRatio="none"><path d="M0 5 Q49 0 98 5 V12 H0Z" fill="#6fb52c"/><path d="M0 8 Q49 3 98 8 V12 H0Z" fill="#1560b5"/></svg>
  </section>

  <section class="piece card-logo" aria-label="Business card logo side">
    <div class="plate"><span class="brand"><span class="dot"></span>Casa Verdant</span></div>
  </section>

  <section class="piece letter letter-a" aria-label="Letterhead">
    <div class="head">
      <span class="brand"><span class="dot"></span>Casa Verdant</span>
      <p class="tag">Indoor Environmental Specialists</p>
    </div>
    <p class="addr">2917 North Quailbrook Ave Unit 248<br>Pinecrest Harbor FL, 33718</p>
    <p class="addr-right">rob@casaverdantcrew.com<br>www.casaverdantcrew.com<br>QTX LKPV391 DWBE PNGH862</p>
    <div class="watermark">Casa Verdant</div>
    <svg class="band" viewBox="0 0 282 40" height="40" preserveAspectRatio="none"><path d="M0 14 Q141 -4 282 14 V40 H0Z" fill="#6fb52c"/><path d="M0 20 Q141 4 282 20 V40 H0Z" fill="#1560b5"/></svg>
  </section>

  <section class="piece letter letter-b" aria-label="Letterhead second page">
    <div class="head">
      <span class="brand"><span class="dot"></span>Casa Verdant</span>
      <p class="tag">Indoor Environmental Specialists</p>
    </div>
    <div class="watermark">Casa Verdant</div>
    <svg class="band" viewBox="0 0 282 40" height="40" preserveAspectRatio="none"><path d="M0 14 Q141 -4 282 14 V40 H0Z" fill="#6fb52c"/><path d="M0 20 Q141 4 282 20 V40 H0Z" fill="#1560b5"/></svg>
    <p class="foot">Serving: Southeast Florida and the Caribbean</p>
  </section>

  <section class="piece env env-green" aria-label="Envelope back green">
    <svg class="flap" viewBox="0 0 344 88" preserveAspectRatio="none">
      <defs><linearGradient id="greenFlap" x1="0" y1="0" x2="0" y2="1"><stop offset="0" stop-color="#3f8f26"/><stop offset="1" stop-color="#a6d14a"/></linearGradient></defs>
      <rect width="344" height="88" fill="#ffffff"/>
      <path d="M0 0 H344 V30 L172 64 L0 30Z" fill="url(#greenFlap)"/>
    </svg>
    <div class="seal"></div>
  </section>

  <section class="piece env env-blue" aria-label="Envelope back blue">
    <svg class="flap" viewBox="0 0 344 86" preserveAspectRatio="none">
      <rect width="344" height="86" fill="#ffffff"/>
      <path d="M0 0 H344 L172 58Z" fill="#1560b5"/>
      <path d="M0 0 H344 L172 50Z" fill="#3a9be0"/>
    </svg>
    <div class="seal"></div>
  </section>

  <section class="piece env env-plain" aria-label="Envelope back white">
    <svg class="flap" viewBox="0 0 360 82" preserveAspectRatio="none"><path d="M0 0 L180 42 L360 0" fill="none" stroke="#d6dce2"/></svg>
  </section>

  <section class="piece env env-front" aria-label="Envelope front">
    <div class="head"><span class="brand"><span class="dot"></span>Casa Verdant</span></div>
    <p class="addr">2917 North Quailbrook Ave Unit 248<br>Pinecrest Harbor FL, 33718<br>www.casaverdantcrew.com</p>
    <svg class="band" viewBox="0 0 378 26" height="26" preserveAspectRatio="none"><path d="M0 10 Q189 -4 378 10 V26 H0Z" fill="#6fb52c"/><path d="M0 15 Q189 2 378 15 V26 H0Z" fill="#1560b5"/></svg>
  </section>

</main>
</body>
</html>
```